Harbour Green Rink Events - Flyer

So now that i have the logo, I need a flyer made up for printing to be delivered to businesses and residential homes.
Below is some information that I want included in the design, in any order and in anyway.
What better way to spend time with family, friends or workmates then to enjoy 2 hours of barefoot bowls.
We can cater for Xmas Parties, Buck's and Hen's Parties, Birthday Parties, Team Building events.
We have food and drink packages to suit all your needs.
So why not come along and have the best fun you can have on 2 feet!
We have 2 locations at Wattlebrook Sports and Bowling Club and Merriden Bowling Club
Prices start from $12pp for 2 hours of lawn bowls fun
Contact Wade Kessler on 0482 157 394 or visit our website www.harbourgreenrinkevents.com.au for more information and to enquire about your function today!

```html
<!DOCTYPE html>
<html lang="en">
<head>
<meta charset="utf-8">
<title>Harbour Green Rink Events – Flyer</title>
<link href="https://fonts.googleapis.com/css2?family=Courgette&family=Amaranth:wght@700&family=Didact+Gothic&family=Kreon:wght@700&family=Mulish:ital,wght@1,300&display=swap" rel="stylesheet">
<style>
  :root {
    --teal: #20aeab;
    --teal-text: #1fa9a6;
    --lime: #a8cc3c;
    --lime-dark: #5f7d14;
    --paper: #f3f3f3;
    --card: #ffffff;
    --ink: #3a3a3a;
    --ink-soft: #4a4a4a;
    --white: #ffffff;
  }
  * { margin: 0; padding: 0; box-sizing: border-box; }
  html, body { width: 1113px; height: 1200px; overflow: hidden; }
  body { background: var(--paper); position: relative; font-family: "Didact Gothic", sans-serif; color: var(--ink-soft); }

  .top-bar, .bottom-bar { position: absolute; left: 0; width: 100%; background: var(--teal); }
  .top-bar { top: 0; height: 44px; }
  .bottom-bar { top: 1153px; height: 47px; }

  .logo-tab { position: absolute; left: 465px; top: 0; width: 167px; height: 143px; }
  .logo-tab span {
    position: absolute; top: 18px; left: 0; width: 100%; text-align: center;
    font-family: "Didact Gothic", sans-serif; font-size: 28px; color: var(--white);
  }

  .intro {
    position: absolute; top: 148px; left: 0; width: 100%; text-align: center;
    font-family: "Courgette", cursive; font-size: 36px; line-height: 53px; color: var(--ink);
    letter-spacing: 1px;
  }

  .offer-card {
    position: absolute; left: 64px; top: 262px; width: 983px; height: 318px;
    background: var(--card);
    box-shadow: 0 6px 14px rgba(0,0,0,0.12);
  }
  .events-band {
    position: absolute; left: 64px; top: 327px; width: 983px; height: 117px;
    background: var(--teal); color: var(--white);
    font-family: "Amaranth", sans-serif; font-weight: 700; font-size: 23px;
    display: flex; align-items: center; justify-content: center;
    white-space: nowrap;
  }
  .ribbon { position: absolute; left: 29px; top: 427px; width: 236px; height: 50px; }
  .ribbon span {
    position: absolute; left: 62px; top: 8px;
    font-family: "Amaranth", sans-serif; font-weight: 700; font-size: 21px; color: var(--ink);
  }
  .package-list {
    position: absolute; left: 124px; top: 500px; list-style: none;
    font-size: 27px; line-height: 37px; color: var(--ink-soft);
  }
  .package-list li::before { content: "➤"; font-size: 17px; margin-right: 12px; vertical-align: 3px; }

  .headline {
    position: absolute; top: 606px; left: 0; width: 100%; text-align: center;
    font-family: "Kreon", serif; font-weight: 700; font-size: 50px; line-height: 56px; color: var(--teal-text);
  }
  .headline strong { color: var(--ink); }

  .locations {
    position: absolute; top: 720px; left: 0; width: 100%; text-align: center;
    font-size: 31px; line-height: 43px; color: var(--ink-soft);
  }

  .price {
    position: absolute; top: 848px; left: 0; width: 100%; text-align: center;
    font-family: "Mulish", sans-serif; font-style: italic; font-weight: 300;
    font-size: 36px; color: var(--teal-text); white-space: nowrap;
  }
  .price u { text-decoration-thickness: 3px; text-underline-offset: 6px; }
  .price .mark { font-style: normal; font-weight: 700; font-size: 30px; margin: 0 10px; vertical-align: 2px; color: var(--teal-text); }

  .contact {
    position: absolute; top: 949px; left: 0; width: 100%; text-align: center;
    font-size: 27px; line-height: 38px; color: var(--ink-soft);
  }
</style>
</head>
<body>
  <div class="top-bar"></div>

  <div class="logo-tab">
    <svg width="167" height="143" viewBox="0 0 167 143">
      <path d="M0 0 H167 V143 Q83.5 66 0 143 Z" fill="#5f7d14"/>
      <path d="M0 0 H167 V133 Q83.5 56 0 133 Z" fill="#a8cc3c"/>
    </svg>
    <span>LOGO</span>
  </div>

  <p class="intro">What better way to spend time with family, friends<br>or workmates then to enjoy 2 hours of barefoot bowls.</p>

  <div class="offer-card"></div>
  <div class="events-band">We can cater for Xmas Parties, Buck's and Hen's Parties, Birthday Parties, Team Building events.</div>

  <div class="ribbon">
    <svg width="236" height="50" viewBox="0 0 236 50">
      <path d="M0 6 L22 10 L22 50 L0 46 L10 26 Z" fill="#6f9221"/>
      <path d="M14 0 H214 L236 24 L214 48 H14 Z" fill="#a8cc3c"/>
      <path d="M20 6 H211 L229 24 L211 42 H20" fill="none" stroke="#e4f2b8" stroke-width="1.5" stroke-dasharray="4 3"/>
    </svg>
    <span>We have :</span>
  </div>

  <ul class="package-list">
    <li>Food</li>
    <li>Drink packages to suit all your needs</li>
  </ul>

  <h1 class="headline">So why not come along and have<br>the best fun you can have on <strong>2 feet</strong>!</h1>

  <p class="locations">We have 2 locations at Wattlebrook Sports<br>and Bowling Club and Merriden Bowling Club</p>

  <p class="price"><span class="mark">›</span><u>Prices start from $12pp for 2 hours of lawn bowls fun</u><span class="mark">‹</span></p>

  <p class="contact">Contact Wade Kessler on 0482 157 394 or visit our website<br>www.harbourgreenrinkevents.com.au for more information<br>and to enquire about your function today!</p>

  <div class="bottom-bar"></div>
</body>
</html>
```